zSTRIDA Membership Flyer

zSTRIDA is a shoe store selling brand name sneakers like Vorn Keltro Brisk Talvan and etc. We need a flyer to promote our membership program. On this flyer we need to emphasize that people who sign up can get 20% off their entire first purchase(certain items are excluded), which is limited time offer.
The flyer is 5.5"X4.25", two sided.
On the back side, there need to be a section where customer can fill up their name, phone number and email to join the membership.
our website is www.zstridashop.example
Member benefits can also be found on the website and should be on the flyer.

Industry/Entity Type

Shoe Store

```html
<!DOCTYPE html>
<html lang="en">
<head>
<meta charset="utf-8">
<title>zSTRIDA Membership Flyer</title>
<link href="https://fonts.googleapis.com/css2?family=Lato:wght@300;400;700;900&family=Oswald:wght@700&family=Arimo:wght@700&display=swap" rel="stylesheet">
<style>
  :root {
    --orange: #e8791b;
    --orange-deep: #c8600e;
    --orange-light: #f39a3c;
    --brown: #5a2e0c;
    --white: #ffffff;
    --ink: #111111;
    --rule: #333333;
  }
  * { margin: 0; padding: 0; box-sizing: border-box; }
  html, body { width: 1200px; height: 464px; overflow: hidden; background: var(--white); }
  .flyer { position: relative; width: 1200px; height: 464px; display: flex; }

  /* Front */
  .front { position: relative; width: 600px; height: 464px; overflow: hidden; color: var(--white); font-family: "Lato", sans-serif; }
  .front-photo {
    position: absolute; inset: 0;
    background:
      radial-gradient(ellipse 60% 40% at 45% 72%, rgba(120,55,10,0.55), transparent 70%),
      radial-gradient(ellipse 50% 60% at 80% 20%, rgba(255,190,110,0.35), transparent 70%),
      linear-gradient(160deg, var(--orange-light) 0%, var(--orange) 45%, var(--orange-deep) 100%);
  }
  .offer { position: absolute; left: 0; right: 0; top: 140px; text-align: center; padding-left: 20px; }
  .offer-join { font-weight: 300; font-size: 36px; letter-spacing: -0.5px; line-height: 1; }
  .offer-brand { font-weight: 900; color: var(--brown); letter-spacing: 0; }
  .offer-amount { font-family: "Oswald", sans-serif; font-weight: 700; font-size: 104px; line-height: 1; margin-top: 2px; letter-spacing: -1px; }
  .offer-scope { font-weight: 300; font-size: 27px; line-height: 1; margin-top: 8px; letter-spacing: -0.3px; }
  .offer-scope strong { font-weight: 900; }
  .offer-note { font-weight: 300; font-size: 21px; line-height: 1; margin-top: 2px; }
  .front-url { position: absolute; left: 0; width: 600px; bottom: 20px; text-align: center; font-family: "Arimo", sans-serif; font-weight: 700; font-size: 15px; letter-spacing: 1.5px; }

  /* Back */
  .back { position: relative; width: 600px; height: 464px; overflow: hidden; background: var(--white); }
  .url-band { position: absolute; left: 0; white-space: nowrap; font-family: "Arimo", sans-serif; font-weight: 700; font-size: 12px; letter-spacing: 1.2px; color: var(--orange-light); word-spacing: 6px; }
  .url-band--top { top: 14px; left: -2px; }
  .url-band--bottom { bottom: 14px; left: -2px; }
  .member-title { position: absolute; left: 57px; top: 64px; font-family: "Lato", sans-serif; font-size: 35px; color: var(--ink); font-weight: 400; line-height: 1; }
  .member-title .brand { color: var(--orange); font-weight: 900; margin-right: 6px; }
  .benefits { position: absolute; left: 57px; top: 126px; width: 520px; font-family: "Arimo", sans-serif; font-weight: 700; color: var(--ink); }
  .benefits-lead { font-size: 13.6px; margin-bottom: 6px; }
  .hl { color: var(--orange); }
  .benefit-list { list-style: none; font-size: 9.6px; line-height: 1.25; }
  .benefit-list li { position: relative; padding-left: 21px; margin-bottom: 5px; }
  .benefit-list .mark { position: absolute; left: 1px; }
  .signup { position: absolute; left: 114px; top: 308px; width: 370px; font-family: "Lato", sans-serif; font-style: italic; font-size: 12.5px; color: var(--ink); }
  .field { display: flex; align-items: flex-end; height: 29px; }
  .field-label { white-space: nowrap; padding-right: 2px; }
  .field-line { flex: 1; border-bottom: 1.6px solid var(--rule); height: 14px; }
</style>
</head>
<body>
<main class="flyer">
  <section class="front">
    <div class="front-photo" role="img" aria-label="Close-up photo of a sneaker on a store shelf, tinted orange"></div>
    <div class="offer">
      <p class="offer-join">JOIN <span class="offer-brand">zSTRIDA</span> AND GET</p>
      <p class="offer-amount">20% OFF</p>
      <p class="offer-scope">YOUR <strong>ENTIRE</strong> FIRST PURCHASE</p>
      <p class="offer-note">(certain items are excluded)</p>
    </div>
    <p class="front-url">www.zstridashop.example</p>
  </section>

  <section class="back">
    <p class="url-band url-band--top">dashop.example www.zstridashop.example www.zstridashop.example www.zstridashop.example www.zstr</p>
    <h1 class="member-title"><span class="brand">ZSTRIDA</span>Membership</h1>
    <div class="benefits">
      <p class="benefits-lead">Benefits: The <span class="hl">ZSTRIDA Member Program</span> entitles Members to the following benefits:</p>
      <ol class="benefit-list">
        <li><span class="mark">a.</span><span class="hl">20% OFF</span> your entire first purchase after you sign up. Certain items are excluded from this offer.<br>Please see stores for details.</li>
        <li><span class="mark">b.</span><span class="hl">10% OFF</span> every purchase while being a member. Certain items are excluded from this offer.<br>Please see stores for details.</li>
        <li><span class="mark">c.</span><span class="hl">Additional 10% OFF</span> and <span class="hl">FREE SHIPPING</span> when an item is out of stock in store but can be shipped to you from another location.</li>
        <li><span class="mark">d.</span>Eligible to purchase exclusive items offered to members only. Purchasing of exclusive items is limited to 1 item per member per 30 days. Please see stores for details.</li>
      </ol>
    </div>
    <div class="signup">
      <div class="field"><span class="field-label">NAME :</span><span class="field-line"></span></div>
      <div class="field"><span class="field-label">NUMBER :</span><span class="field-line"></span></div>
      <div class="field"><span class="field-label">EMAIL :</span><span class="field-line"></span></div>
    </div>
    <p class="url-band url-band--bottom">www.zstridashop.example www.zstridashop.example www.zstridashop.example www.zstridashop.example www.</p>
  </section>
</main>
</body>
</html>
```